Acupuncture business needs business card design

I need a business card for an acupuncture clinic called "Summit Wellpath"
It will need the following details:
My name: Marcus Thelwick
Acupuncturist
Member KPTG
BVF Treatment Provider
Ph numbers: 482 1358 027 514 3820
Email: marcus@swpath.example.nz
On the back it will need a table with 2 columns for appointments, one column for time and one for date.

Industry/Entity Type

Clinic

Contact Information for Business Card

Marcus Thelwick
Acupuncturist
Member KPTG
BVF Treatment Provider
Email: marcus@swpath.example.nz

Requirements
Must have
• Marcus Thelwick
• Acupuncturist
• Member KPTG
• BVF Treatment Provider
• Ph numbers: 482 1358 027 514 3820
• Email: marcus@swpath.example.nz
• On the back it will need a table with 2 columns for appointments, one column for time and one for date.

```html
<!DOCTYPE html>
<html lang="en">
<head>
<meta charset="utf-8">
<title>Summit Wellpath – Double-Sided Business Card</title>
<link rel="stylesheet" href="https://fonts.googleapis.com/css2?family=Questrial&family=Roboto+Condensed:wght@700&display=swap">
<style>
  :root {
    --page: #ffffff;
    --ink: #111111;
    --rule: #8c8c8c;
    --card-edge: #9a9a9a;
    --brand-light: #27a8df;
    --brand-deep: #157f92;
    --grid-line: #3b8fa6;
  }
  * { margin: 0; padding: 0; box-sizing: border-box; }
  html, body { width: 1200px; height: 848px; overflow: hidden; background: var(--page); }
  .sheet { position: relative; width: 1200px; height: 848px; }

  .sheet-title {
    position: absolute; left: 245px; top: 139px;
    font: 700 12px/1 "Roboto Condensed", sans-serif; color: var(--ink); letter-spacing: .2px;
  }
  .sheet-rule { position: absolute; left: 245px; top: 154px; width: 712px; height: 1px; background: var(--rule); }
  .sheet-size {
    position: absolute; left: 245px; top: 162px;
    font: 700 9px/1 "Roboto Condensed", sans-serif; color: var(--ink);
  }
  .side-label {
    position: absolute; top: 608px;
    font: 700 8px/1 "Roboto Condensed", sans-serif; color: var(--ink); transform: translateX(-50%);
  }

  .card { position: absolute; border: 1px solid var(--card-edge); background: #fff; }
  .card-front { left: 260px; top: 392px; width: 360px; height: 203px; }
  .card-back { left: 674px; top: 255px; width: 203px; height: 345px; }

  .brand { position: absolute; left: 44px; top: 26px; display: flex; align-items: center; gap: 12px; }
  .brand-dot { width: 26px; height: 26px; border-radius: 50%; background: var(--brand-deep); }
  .brand-name { font: 400 22px/1 "Questrial", sans-serif; color: var(--brand-light); }

  .holder { position: absolute; left: 83px; top: 77px; font-family: "Questrial", sans-serif; color: var(--ink); }
  .holder-name { font-size: 15px; line-height: 18px; }
  .holder-role { font-size: 10.5px; line-height: 12px; }

  .contact { position: absolute; left: 83px; top: 152px; font: 400 10.5px/12px "Questrial", sans-serif; color: var(--ink); }
  .contact b { display: inline-block; width: 10px; font-weight: 700; }

  .back-art { position: absolute; left: 0; top: 0; }
  .back-art text.col-head { font: 400 10px "Questrial", sans-serif; fill: var(--brand-light); }

  .back-brand {
    position: absolute; left: 165px; top: 26px;
    writing-mode: vertical-rl; font: 400 16px/1 "Questrial", sans-serif; color: var(--brand-light);
  }
  .back-tab-label {
    position: absolute; left: 160px; top: 204px;
    writing-mode: vertical-rl; font: 400 10px/1 "Questrial", sans-serif; color: #fff; letter-spacing: 2.6px;
  }
</style>
</head>
<body>
<main class="sheet">
  <h1 class="sheet-title">DOUBLE-SIDED BUSINESS CARD DESIGN</h1>
  <div class="sheet-rule"></div>
  <p class="sheet-size">Size: 50mm (W) x 85mm (H)</p>

  <section class="card card-front" aria-label="Card front">
    <div class="brand">
      <span class="brand-dot"></span>
      <span class="brand-name">Summit Wellpath</span>
    </div>
    <div class="holder">
      <p class="holder-name">Marcus Thelwick</p>
      <p class="holder-role">Acupuncturist</p>
      <p class="holder-role">Member KPTG</p>
      <p class="holder-role">BVF Treatment Provider</p>
    </div>
    <div class="contact">
      <p><b>m</b>: 482 1358 027 514 3820</p>
      <p><b>e</b>&nbsp;: marcus@swpath.example.nz</p>
    </div>
  </section>
  <p class="side-label" style="left:440px">FRONT</p>

  <section class="card card-back" aria-label="Card back – appointment table">
    <svg class="back-art" width="203" height="345" viewBox="0 0 203 345">
      <g fill="none" stroke="var(--grid-line)" stroke-width="0.8">
        <rect x="14" y="15" width="136" height="315"/>
        <line x1="82" y1="15" x2="82" y2="330"/>
        <line x1="14" y1="35" x2="150" y2="35"/>
        <line x1="14" y1="56" x2="150" y2="56"/>
        <line x1="14" y1="77" x2="150" y2="77"/>
        <line x1="14" y1="98" x2="150" y2="98"/>
        <line x1="14" y1="119" x2="150" y2="119"/>
        <line x1="14" y1="140" x2="150" y2="140"/>
        <line x1="14" y1="161" x2="150" y2="161"/>
        <line x1="14" y1="182" x2="150" y2="182"/>
        <line x1="14" y1="203" x2="150" y2="203"/>
        <line x1="14" y1="224" x2="150" y2="224"/>
        <line x1="14" y1="245" x2="150" y2="245"/>
        <line x1="14" y1="266" x2="150" y2="266"/>
        <line x1="14" y1="287" x2="150" y2="287"/>
        <line x1="14" y1="308" x2="150" y2="308"/>
        <path d="M150 15 H152 Q156 15 156 19" stroke="var(--brand-deep)" stroke-width="1.2"/>
        <path d="M150 15 V170 Q150 180 160 184 L176 190" stroke="var(--brand-deep)" stroke-width="1.2"/>
      </g>
      <path d="M150 170 Q150 180 160 184 L178 191 Q188 195 188 206 V325 Q188 330 183 330 H150 Z" fill="var(--brand-deep)"/>
      <text class="col-head" x="48" y="29" text-anchor="middle">Time</text>
      <text class="col-head" x="116" y="29" text-anchor="middle">Date</text>
    </svg>
    <span class="back-brand">Summit Wellpath</span>
    <span class="back-tab-label">Appointments</span>
  </section>
  <p class="side-label" style="left:776px">BACK</p>
</main>
</body>
</html>
```